Price Package PDF - 2 page PDF of stylized price packages for property management firm

Looking for a 2 x A4 page PDF for our two price packages.
I would like this to be in similar style to our website www.harbourlanerentals.com.au
I have attached an example. But would like mine to be a little more stylish and modern, preferably using design similar to our website.
Words and images also attached

Target Market(s)

investment property owners, male and female, aged 30-60

Industry/Entity Type

Real Estate

Font styles to use
Sans Serif

Requirements
Must have
• split two packages onto seperate A4 pages (See example file attached)
• Contact info:
• Website: www.harbourlanerentals.com.au
• email: info@harbourlanerentals.com.au
• Phone: Tom Radley 0417 562 903, Larisa Okonjo 0409 317 648
• Office Address: Suite 7, 12-14 Wattle Parade, Curl Curl NSW 2096
Nice to have
• I would like to use any of the pictures provided or images of modern residential property interior or of Sydney's Northern Beaches.

```html
<!DOCTYPE html>
<html lang="en">
<head>
<meta charset="utf-8">
<title>Harbour Lane Rentals – Price Packages</title>
<link href="https://fonts.googleapis.com/css2?family=Montserrat:wght@300;400;500;600;700&display=swap" rel="stylesheet">
<style>
  :root{
    --backdrop:#3b3c3e;
    --teal:#1c7c8b;
    --teal-mid:#24808f;
    --teal-dark:#0f5a68;
    --teal-deep:#0b4f5c;
    --cyan:#4cc3cb;
    --text-light:#e6f4f6;
    --white:#ffffff;
  }
  *{box-sizing:border-box;margin:0;padding:0}
  html,body{width:1200px;height:800px;overflow:hidden}
  body{background:var(--backdrop);font-family:"Montserrat",Arial,sans-serif;position:relative}
  .page{position:absolute;top:50px;width:587px;height:830px;transform:scale(.843);transform-origin:top left;overflow:hidden;background:var(--white);box-shadow:0 14px 28px rgba(0,0,0,.45)}
  .page--inclusive{left:70px}
  .page--lease{left:635px;background:var(--teal-dark)}
  .art{position:absolute;inset:0;width:587px;height:830px}
  .brand{position:absolute;left:42px;top:216px;color:var(--white)}
  .brand__name{font-size:36px;font-weight:600;letter-spacing:.3px;line-height:1;text-shadow:0 1px 3px rgba(0,0,0,.35)}
  .brand__sub{display:block;text-align:right;font-size:11px;font-weight:400;margin-top:6px;letter-spacing:.4px}
  .heading{position:absolute;color:var(--white);line-height:1.05}
  .heading strong{font-weight:700;display:block;font-size:21px;letter-spacing:.3px}
  .heading span{font-weight:300;display:block;font-size:25px}
  .bar{position:absolute;height:23px;background:var(--cyan);color:var(--white);font-size:16px;line-height:23px;font-weight:500;letter-spacing:.3px}
  .bar b{font-weight:700}
  .bar .thin{font-weight:300}
  .list{position:absolute;list-style:none;color:var(--text-light);font-size:10.6px;font-weight:400;line-height:15.8px}
  .list li{position:relative;padding-left:8px}
  .list li::before{content:"";position:absolute;left:0;top:7px;width:3px;height:3px;border-radius:50%;background:var(--cyan)}
  .list .lead{font-weight:600;color:var(--white)}
  .list--right li{padding-left:0;padding-right:9px;text-align:right}
  .list--right li::before{left:auto;right:0}
  .list--right li.plain::before{display:none}
  .photo{position:absolute;border:2px solid var(--white)}
  .contact{position:absolute;font-size:8.6px;line-height:12.4px;font-weight:400;font-style:normal}
  .contact b{font-weight:600}
  .contact--dark{color:var(--teal-deep)}
  .contact--light{color:var(--text-light)}
</style>
</head>
<body>

<section class="page page--inclusive">
  <svg class="art" viewBox="0 0 587 830">
    <defs>
      <linearGradient id="gPool" x1="0" y1="0" x2="0" y2="1">
        <stop offset="0" stop-color="#8fc4e2"/><stop offset=".35" stop-color="#2e6f8e"/><stop offset="1" stop-color="#4fa39d"/>
      </linearGradient>
      <linearGradient id="gHouses" x1="0" y1="0" x2="0" y2="1">
        <stop offset="0" stop-color="#6db5e0"/><stop offset=".45" stop-color="#c9d3d6"/><stop offset="1" stop-color="#5f7d4f"/>
      </linearGradient>
      <linearGradient id="gGarden" x1="0" y1="0" x2="0" y2="1">
        <stop offset="0" stop-color="#5e7d4c"/><stop offset=".55" stop-color="#d2dbcf"/><stop offset=".75" stop-color="#ffffff"/>
      </linearGradient>
    </defs>
    <g role="img" aria-label="Photo of an ocean rock pool with a sculpture">
      <polygon points="0,0 380,0 310,205 0,150" fill="url(#gPool)"/>
    </g>
    <g role="img" aria-label="Photo of modern beachside townhouses">
      <polygon points="380,0 587,0 587,352 302,284 310,205" fill="url(#gHouses)"/>
    </g>
    <g role="img" aria-label="Photo of a landscaped garden and stairway">
      <polygon points="0,150 310,205 302,284 170,520 0,420" fill="url(#gGarden)"/>
    </g>
    <polygon points="302,284 587,352 587,830 0,830 0,800" fill="var(--teal)"/>
    <polygon points="0,830 0,760 60,690 95,830" fill="var(--teal-dark)"/>
    <polygon points="587,680 587,830 420,830" fill="var(--teal-mid)"/>
  </svg>

  <div class="brand">
    <div class="brand__name">HARBOUR LANE</div>
    <span class="brand__sub">RENTALS</span>
  </div>

  <address class="contact contact--dark" style="left:16px;top:436px;width:160px">
    www.harbourlanerentals.com.au<br>
    info@harbourlanerentals.com.au<br>
    <b>Tom Radley</b> 0417 562 903<br>
    <b>Larisa Okonjo</b> 0409 317 648<br>
    Suite 7, 12-14 Wattle Parade,<br>
    Curl Curl NSW 2096
  </address>

  <div class="heading" style="left:277px;top:322px"><strong>ALL INCLUSIVE</strong><span>PACKAGE:</span></div>

  <div class="bar" style="left:279px;top:376px;width:308px;padding-left:13px">INCLUDES:</div>
  <ul class="list" style="left:284px;top:400px;width:300px">
    <li>Securing Tenant</li>
    <li>Reference/Database Checking</li>
    <li>Lease Preparation and Signing</li>
    <li>Direct Debit rent collection</li>
    <li>Zero arrears policy management</li>
    <li>Payment of Rates and levies</li>
    <li>Insurance management</li>
    <li>Coordination or all repairs and maintenance</li>
    <li>Regular rent reviews and renewals</li>
    <li>Detailed ingoing, ongoing and outgoing inspections with photos and videos – viewable through your personal Landlord portal</li>
    <li>Bond management – lodging and refunding</li>
    <li>Electronic monthly and EOFY statements</li>
    <li>Annual scheduled maintenance report</li>
    <li>Regulation/compliance management</li>
    <li>Tribunal Representation</li>
  </ul>

  <svg class="photo" style="left:96px;top:555px;width:157px;height:131px" viewBox="0 0 157 131" role="img" aria-label="Photo of a harbour with moored boats">
    <defs><linearGradient id="gBay" x1="0" y1="0" x2="0" y2="1"><stop offset="0" stop-color="#2e8fd0"/><stop offset=".55" stop-color="#9fc9e6"/><stop offset="1" stop-color="#1f5f85"/></linearGradient></defs>
    <rect width="157" height="131" fill="url(#gBay)"/>
  </svg>
  <svg class="photo" style="left:24px;top:640px;width:158px;height:131px" viewBox="0 0 158 131" role="img" aria-label="Photo of a modern two-storey home with garden">
    <defs><linearGradient id="gHome" x1="0" y1="0" x2="0" y2="1"><stop offset="0" stop-color="#3f9bd8"/><stop offset=".5" stop-color="#c8ccc8"/><stop offset="1" stop-color="#55713f"/></linearGradient></defs>
    <rect width="158" height="131" fill="url(#gHome)"/>
  </svg>

  <div class="bar" style="left:279px;top:674px;width:308px;height:28px;line-height:28px;font-size:18px;padding-left:11px"><b>ALL INCLUSIVE</b> <span class="thin">PACKAGE:</span></div>
  <ul class="list" style="left:284px;top:706px;width:300px">
    <li class="lead">Management Rate: 10% + GST of rental income</li>
    <li>Letting Fee: No Charge</li>
    <li>Advertising: No Charge</li>
    <li>Professional Photography: $199 (inc GST) 4 x Photos</li>
    <li>Statements: No Charge</li>
    <li>Lease Preperation: No Charge</li>
    <li>Renewal Fees: No Charge</li>
  </ul>
</section>

<section class="page page--lease">
  <svg class="art" viewBox="0 0 587 830">
    <defs>
      <linearGradient id="gHarbour" x1="0" y1="0" x2="0" y2="1">
        <stop offset="0" stop-color="#2a86c8"/><stop offset=".4" stop-color="#5b8f8a"/><stop offset=".7" stop-color="#1f6fa3"/><stop offset="1" stop-color="#3d6b78"/>
      </linearGradient>
      <linearGradient id="gBeach" x1="0" y1="0" x2="0" y2="1">
        <stop offset="0" stop-color="#e9eef0"/><stop offset=".45" stop-color="#a8b4a4"/><stop offset="1" stop-color="#6e8e98"/>
      </linearGradient>
      <linearGradient id="gShore" x1="0" y1="0" x2="0" y2="1">
        <stop offset="0" stop-color="#93c3e6"/><stop offset=".45" stop-color="#e4eef4"/><stop offset=".6" stop-color="#3c7fa6"/><stop offset="1" stop-color="#1f5d7d"/>
      </linearGradient>
    </defs>
    <g role="img" aria-label="Photo of a harbour marina with yachts">
      <polygon points="0,0 380,0 290,357 0,357" fill="url(#gHarbour)"/>
    </g>
    <g role="img" aria-label="Photo of a beach and ocean pool with apartments">
      <polygon points="380,0 587,0 587,357 290,357" fill="url(#gBeach)"/>
    </g>
    <rect x="0" y="335" width="587" height="22" fill="var(--teal-dark)" opacity=".55"/>
    <rect x="0" y="376" width="276" height="262" fill="var(--teal-mid)"/>
    <g role="img" aria-label="Photo of a calm bay and headland">
      <rect x="287" y="676" width="300" height="154" fill="url(#gShore)"/>
    </g>
  </svg>

  <div class="brand">
    <div class="brand__name">HARBOUR LANE</div>
    <span class="brand__sub">RENTALS</span>
  </div>

  <div class="heading" style="left:49px;top:420px"><strong style="font-size:23px;line-height:1.3">LEASE AND<br>MANAGEMENT</strong><span style="font-size:28px">PACKAGE:</span></div>

  <address class="contact contact--light" style="left:49px;top:528px;width:220px">
    www.harbourlanerentals.com.au<br>
    info@harbourlanerentals.com.au<br>
    <b>Tom Radley</b> 0417 562 903<br>
    <b>Larisa Okonjo</b> 0409 317 648<br>
    Suite 7, 12-14 Wattle Parade,<br>
    Curl Curl NSW 2096
  </address>

  <div class="bar" style="left:287px;top:376px;width:300px;padding-left:13px">INCLUDES:</div>
  <ul class="list" style="left:292px;top:400px;width:292px">
    <li>Securing Tenant</li>
    <li>Reference/Database Checking</li>
    <li>Lease Preparation and Signing</li>
    <li>Direct Debit rent collection</li>
    <li>Zero arrears policy management</li>
    <li>Payment of Rates and levies</li>
    <li>Insurance management</li>
    <li>Coordination or all repairs and maintenance</li>
    <li>Regular rent reviews and renewals</li>
    <li>Detailed ingoing, ongoing and outgoing inspections with photos and videos – viewable through your personal Landlord portal</li>
    <li>Bond management – lodging and refunding</li>
    <li>Electronic monthly and EOFY statements</li>
    <li>Annual scheduled maintenance report</li>
    <li>Regulation/compliance management</li>
    <li>Tribunal Representation</li>
  </ul>

  <div class="bar" style="left:0;top:646px;width:276px;height:28px;line-height:28px;font-size:17px;text-align:right;padding-right:6px"><b>MANAGEMENT</b> <span class="thin">RATE:</span></div>
  <ul class="list list--right" style="left:0;top:680px;width:276px">
    <li class="lead plain">Management Rate: 6% +GST of rental income</li>
    <li>Letting Fee:</li>
    <li class="plain">- 1 weeks rent +GST 6 or 12 month lease</li>
    <li>Advertising: $350 (Inc GST)</li>
    <li>Professional Photography:</li>
    <li class="plain"><span class="lead">$199</span> (inc GST) 4 x Photos</li>
    <li>Statements: $5.00 Per month</li>
    <li>Lease Preperation: No Charge</li>
    <li>Renewal Fees: ½ Weeks Rent +GST</li>
  </ul>
</section>

</body>
</html>
```